Moder Business Card Design for Renewables Business

Need a business card design for my business. We collect & repurpose spent coffee ground from cafes. The cards will be made from recycled paper. Needs to fit our corporate colour scheme of white, green & brown (see logo for colour codes). Eco friendly, modern, intresting & eye catching.
This card needs to convey the message of the business and fit into its mantra of eco-friendly, sustainable etc.

Target Market(s)

Cafe Owners, Coffee Drinkers, Recycling Companies, Farmers

Industry/Entity Type

Recycling

Contact Information for Business Card

Name; Peter Dalton
Phone; 0438 216 570
e-mail; info@florivex.com.au
website; www.florivex.com.au

Font styles to use
Sans Serif
Script

Colors

Designer to choose colors to be used in the design.

Requirements
Must have
• FRONT;
• Logo, Name (Peter Dalton), phone number, e-mail address, website
• BACK;
• On the back in cursive text; 'GREENER HABITS IN EVERY SINGLE CUP'
• Small facebook & Instagram logos with text 'Florivex'
Should not have
• messy design

```html
<!DOCTYPE html>
<html lang="en">
<head>
<meta charset="utf-8">
<title>Florivex Business Card</title>
<link href="https://fonts.googleapis.com/css2?family=Berkshire+Swash&family=Open+Sans:wght@600;700&family=Roboto:wght@400;500&display=swap" rel="stylesheet">
<style>
  :root {
    --backdrop: #2b2b2b;
    --paper: #ebe8e2;
    --brown: #7a4a1f;
    --green: #6aa53a;
  }
  * { box-sizing: border-box; margin: 0; padding: 0; }
  html, body {
    width: 1200px; height: 900px; overflow: hidden;
    background: var(--backdrop);
  }
  .canvas {
    width: 1200px; height: 900px;
    display: flex; flex-direction: column; align-items: center;
    justify-content: center; gap: 48px;
  }
  .card {
    width: 640px; height: 366px;
    background: var(--paper);
    border-radius: 26px;
    position: relative;
    box-shadow: 0 10px 24px rgba(0,0,0,.35);
  }
  /* Front */
  .brand {
    position: absolute; left: 40px; top: 96px; width: 262px;
    display: flex; flex-direction: column; align-items: center; gap: 10px;
  }
  .brand-dot {
    width: 92px; height: 92px; border-radius: 50%;
    background: var(--green);
  }
  .brand-name {
    font-family: "Open Sans", sans-serif; font-weight: 600;
    font-size: 30px; letter-spacing: 1px; text-transform: uppercase;
    color: var(--green);
  }
  .divider {
    position: absolute; left: 322px; top: 118px;
    width: 2px; height: 150px; background: var(--brown);
  }
  .contact {
    position: absolute; left: 350px; top: 124px;
    color: var(--brown);
  }
  .person-name {
    font-family: "Open Sans", sans-serif; font-weight: 700;
    font-size: 22px; text-transform: uppercase; letter-spacing: .5px;
    line-height: 1.1;
  }
  .person-role {
    font-family: "Roboto", sans-serif; font-size: 14px; margin-bottom: 14px;
  }
  .contact-list { list-style: none; }
  .contact-item {
    display: flex; align-items: center; gap: 10px;
    font-family: "Roboto", sans-serif; font-size: 16px;
    margin-bottom: 8px;
  }
  .contact-icon { width: 18px; height: 18px; flex: none; }
  /* Back */
  .tagline {
    position: absolute; left: 0; right: 0; top: 100px;
    text-align: center;
    font-family: "Berkshire Swash", cursive;
    font-size: 28px; color: var(--brown);
  }
  .social {
    position: absolute; left: 0; right: 0; top: 156px;
    display: flex; flex-direction: column; align-items: center; gap: 6px;
    font-family: "Roboto", sans-serif; font-size: 15px; color: var(--brown);
  }
  .social-dot {
    width: 14px; height: 14px; border-radius: 50%; background: var(--brown);
  }
</style>
</head>
<body>
<main class="canvas">
  <section class="card card-front" aria-label="Card front">
    <div class="brand">
      <span class="brand-dot"></span>
      <span class="brand-name">Florivex</span>
    </div>
    <div class="divider"></div>
    <div class="contact">
      <h1 class="person-name">Peter Dalton</h1>
      <p class="person-role">Managing Director</p>
      <ul class="contact-list">
        <li class="contact-item">
          <svg class="contact-icon" viewBox="0 0 18 18"><circle cx="9" cy="9" r="9" fill="#7a4a1f"/><path d="M5.5 5.2c.6-.6 1.2-.5 1.5 0l.9 1.4c.2.4.1.8-.2 1.1l-.5.4c.4 1 1.2 1.8 2.2 2.2l.4-.5c.3-.3.7-.4 1.1-.2l1.4.9c.5.3.6.9 0 1.5-.9.9-2.4.8-4.2-.6-1.7-1.4-3-3.1-3-4.4 0-.7.1-1.3.4-1.8z" fill="#fff"/></svg>
          <span>0438 216 570</span>
        </li>
        <li class="contact-item">
          <svg class="contact-icon" viewBox="0 0 18 18"><circle cx="9" cy="9" r="9" fill="#7a4a1f"/><rect x="4.5" y="6" width="9" height="6.5" rx="1" fill="none" stroke="#fff" stroke-width="1.2"/><polyline points="4.8,6.4 9,9.6 13.2,6.4" fill="none" stroke="#fff" stroke-width="1.2"/></svg>
          <span>info@florivex.com.au</span>
        </li>
        <li class="contact-item">
          <svg class="contact-icon" viewBox="0 0 18 18"><circle cx="9" cy="9" r="9" fill="#7a4a1f"/><rect x="4.2" y="7.2" width="5.4" height="3.6" rx="1.8" fill="none" stroke="#fff" stroke-width="1.2" transform="rotate(-45 6.9 9)"/><rect x="8.4" y="7.2" width="5.4" height="3.6" rx="1.8" fill="none" stroke="#fff" stroke-width="1.2" transform="rotate(-45 11.1 9)"/></svg>
          <span>www.florivex.com.au</span>
        </li>
      </ul>
    </div>
  </section>

  <section class="card card-back" aria-label="Card back">
    <p class="tagline">Greener Habits In Every Single Cup</p>
    <div class="social">
      <span class="social-dot"></span>
      <span>Florivex</span>
    </div>
  </section>
</main>
</body>
</html>
```